Law firm Seeks Modern and Engaging Site Redesign

Law firm seeks a new web site. Should be modern, but retaining existing logo. Needs to include contact section, professional bio, services offered, and contact information.

The site should be modern, responsive, and able to be SEO optimized.

The finished product should be coded in a Wordpress site, which I will provide. I can work with other platforms, including Wix, but WP is preferred.

Note the current site is https://www.tallowfieldlaw.example/#/home

Target Market(s)

Family Law Practice

Industry/Entity Type

Legal

Coding

Coded - Design and coding required

Number of Pages Required

4 page

Font styles to use
Sans Serif

Requirements
Must have
• Service description
Bio pages for partners
Contact Form
Awards/Publication page

```html
<!DOCTYPE html>
<html lang="en">
<head>
<meta charset="utf-8">
<title>Tallowfield Hartley – Family Law Practice</title>
<link href="https://fonts.googleapis.com/css2?family=Domine:wght@400;700&family=Montserrat:ital,wght@0,400;0,500;0,600;0,700;1,400&family=Roboto:wght@400;500&display=swap" rel="stylesheet">
<style>
:root{
  --navy:#3e4a8f;
  --blue:#5a7be0;
  --ink:#222;
  --text:#555;
  --gray-bg:#f2f2f2;
  --line:#e2e2e2;
  --gold:#9a7b55;
  --dark:#2d2d2d;
  --white:#fff;
}
*{box-sizing:border-box;margin:0;padding:0}
html,body{width:1200px;height:4264px;overflow:hidden}
body{position:relative;font-family:'Montserrat',sans-serif;color:var(--text);background:var(--white)}
.abs{position:absolute}
.section-title{position:absolute;left:0;width:1200px;text-align:center;font-family:'Domine',serif;font-weight:400;color:var(--navy);font-size:36px}
.rule{position:absolute;left:576px;width:48px;height:3px;background:var(--navy)}

.topbar{top:0;left:0;width:1200px;height:33px;background:var(--navy);color:#fff;font-size:11px;font-weight:600;letter-spacing:.3px}
.topbar .item{position:absolute;top:8px;display:flex;align-items:center;gap:8px}
.topbar .dot{width:18px;height:18px;border-radius:50%;background:#fff;display:flex;align-items:center;justify-content:center}

.nav{top:33px;left:0;width:1200px;height:58px;background:#fff;border-bottom:1px solid var(--line)}
.brand{position:absolute;left:141px;top:15px;font-size:21px;color:#666;font-weight:500}
.menu{position:absolute;top:22px;font-size:12.5px;color:#222;font-weight:500}
.menu.active{color:var(--blue)}

.hero{top:91px;left:0;width:1200px;height:530px;background:linear-gradient(90deg,#8f959c 0%,#c9cdd1 30%,#dadde0 55%,#b9bcbf 75%,#6e5f51 92%,#4b3e33 100%)}
.hero-name{top:70px;left:0;width:1200px;text-align:center;font-family:'Domine',serif;font-size:72px;color:rgba(255,255,255,.55)}
.hero-title{top:188px;left:0;width:1200px;text-align:center;font-family:'Domine',serif;font-size:52px;color:#111;font-weight:400}
.hero-sub{top:258px;left:0;width:1200px;text-align:center;font-size:13px;line-height:20px;color:#222;font-weight:500}
.btn{position:absolute;background:var(--blue);color:#fff;border-radius:20px;font-size:11px;font-weight:600;text-align:center;letter-spacing:.3px}
.hero .btn{top:329px;left:544px;width:112px;height:33px;line-height:33px}
.scroll-tab{top:500px;left:580px;width:40px;height:30px;border-radius:20px 20px 0 0;background:var(--gray-bg)}

.awards{top:621px;left:0;width:1200px;height:245px;background:var(--gray-bg)}
.badge{position:absolute;background:#d4d4d4}

.about-frame{top:938px;left:142px;width:341px;height:386px;border:3px solid var(--navy)}
.about-photo{top:952px;left:160px;width:353px;height:380px;background:linear-gradient(135deg,#6d5b4b,#b3a190 50%,#e6e0d8)}
.years-box{top:1177px;left:311px;width:240px;height:225px;background:#fff;border:6px solid var(--gold);border-image:linear-gradient(135deg,#c4a57a,#6b5235) 1}
.years-box .have{position:absolute;top:26px;left:22px;color:var(--blue);font-size:15px}
.years-box .num{position:absolute;top:38px;left:20px;font-size:118px;font-weight:500;color:#111;letter-spacing:-4px;line-height:120px}
.years-box .plus{position:absolute;top:148px;left:132px;color:var(--blue);font-size:18px;font-weight:500}
.years-box .exp{position:absolute;top:173px;left:28px;color:var(--blue);font-size:20px;font-weight:500}
.hatch{top:1192px;left:540px;width:24px;height:224px;background:repeating-linear-gradient(45deg,#ccc 0 1px,transparent 1px 5px)}
.hatch2{top:1402px;left:326px;width:238px;height:14px;background:repeating-linear-gradient(45deg,#ccc 0 1px,transparent 1px 5px)}
.about-title{top:994px;left:619px;font-family:'Domine',serif;font-size:38px;color:var(--navy);font-weight:400}
.about-rule{top:1045px;left:619px;width:48px;height:3px;background:var(--navy)}
.about-text{top:1068px;left:619px;width:442px;font-size:11px;line-height:22.5px;color:#555}
.about-text p+p{margin-top:12px}
.about .btn{top:1315px;left:619px;width:114px;height:34px;line-height:34px}

.services-bg{top:1486px;left:0;width:1200px;height:360px;background:var(--gray-bg)}
.tab{position:absolute;top:1632px;height:36px;line-height:36px;border-radius:20px;font-size:11.5px;font-weight:600;color:#fff;text-align:center}
.card{position:absolute;top:1701px;width:173px;height:227px;background:#fff;box-shadow:0 1px 4px rgba(0,0,0,.15)}
.card .ph{position:absolute;top:6px;left:6px;width:161px;height:142px}
.card h3{position:absolute;top:162px;left:0;width:100%;text-align:center;font-family:'Domine',serif;font-weight:400;font-size:15px;color:var(--navy)}
.card p{position:absolute;top:187px;left:12px;width:149px;text-align:center;font-size:9.5px;line-height:13px;color:#666}
.arrow-btn{position:absolute;width:26px;height:26px;border-radius:50%}

.member{position:absolute;top:2089px;width:199px;height:327px;background:#fff;border:1px solid #ddd;box-shadow:0 0 0 3px #f4f4f4}
.member.featured{border-color:var(--blue)}
.member .ph{position:absolute;top:6px;left:6px;width:185px;height:205px}
.member h4{position:absolute;top:234px;width:100%;text-align:center;font-size:13px;font-weight:700;color:#222}
.member.featured h4{color:var(--blue)}
.member .role{position:absolute;top:254px;width:100%;text-align:center;font-size:11px;color:#666}
.member .social{position:absolute;top:284px;left:0;width:100%;display:flex;justify-content:center;gap:11px;align-items:center}
.member .social i{display:block;width:12px;height:12px;border-radius:50%;background:#5b6a9e}

.cta{top:2489px;left:0;width:1200px;height:300px;background:linear-gradient(90deg,#5673d6,#6a88e6 50%,#5c78d9)}
.cta h2{position:absolute;top:66px;width:100%;text-align:center;font-family:'Domine',serif;font-weight:400;font-size:36px;color:#fff}
.cta .cta-rule{position:absolute;top:120px;left:584px;width:32px;height:2px;background:#fff}
.cta p{position:absolute;top:130px;left:240px;width:720px;text-align:center;font-size:11.5px;line-height:20px;color:#fff;font-weight:600;letter-spacing:.2px}
.pill{position:absolute;top:187px;left:417px;width:366px;height:43px;border-radius:8px;background:#fff;display:flex;align-items:center;justify-content:center;gap:10px;font-size:16px;color:#222}

.t-photo{top:2861px;left:437px;width:622px;height:417px;background:linear-gradient(90deg,#9c9c9c,#cfcfcf 40%,#bdbdbd 70%,#a8a8a8)}
.t-card{top:2964px;left:141px;width:596px;height:368px;background:#fff;box-shadow:0 2px 10px rgba(0,0,0,.12)}
.t-card h2{position:absolute;top:52px;left:27px;font-family:'Domine',serif;font-weight:400;font-size:36px;color:var(--navy)}
.t-card .t-rule{position:absolute;top:111px;left:27px;width:40px;height:3px;background:var(--navy)}
.t-card blockquote{position:absolute;top:136px;left:27px;width:540px;font-size:11.5px;line-height:21.5px;font-style:italic;color:#555}
.t-card .who{position:absolute;top:318px;left:27px;font-size:15px;font-weight:700;color:var(--blue)}
.t-arrow{position:absolute;left:703px;width:35px;height:27px;background:var(--blue);display:flex;align-items:center;justify-content:center}

.map{top:3434px;left:0;width:1200px;height:535px;background:linear-gradient(135deg,#eef0ee,#e6e8e6 50%,#eff1ef)}
.map-line{top:3969px;left:0;width:1200px;height:3px;background:var(--blue)}
.contact{top:3515px;left:141px;width:432px;height:388px;background:var(--dark);color:#fff;font-family:'Roboto',sans-serif}
.contact h2{position:absolute;top:55px;left:38px;font-size:28px;font-weight:500;letter-spacing:.3px}
.contact .c-rule{position:absolute;top:98px;left:38px;width:48px;height:3px;background:#fff}
.c-item{position:absolute;left:38px;display:flex;gap:14px;font-size:13.5px;line-height:18px}
.c-item svg{flex:none;margin-top:1px}

.f-link{position:absolute;top:4026px;font-size:12px;color:#333}
.f-link.active{font-weight:700;color:#111}
.f-brand{top:4081px;left:0;width:1200px;text-align:center;font-size:29px;color:#666}
.disclaimer{top:4144px;left:230px;width:740px;text-align:center;font-size:10px;line-height:17px;color:#777}
.bottom{top:4217px;left:0;width:1200px;height:47px;background:var(--navy);color:#fff;font-size:12px;text-align:center;line-height:47px}
</style>
</head>
<body>

<div class="abs topbar">
  <div class="item" style="left:141px">
    <span class="dot"><svg width="10" height="10" viewBox="0 0 24 24"><path fill="#3e4a8f" d="M6.6 10.8a15 15 0 006.6 6.6l2.2-2.2a1 1 0 011-.25 11.4 11.4 0 003.6.6 1 1 0 011 1V20a1 1 0 01-1 1A17 17 0 013 4a1 1 0 011-1h3.5a1 1 0 011 1 11.4 11.4 0 00.6 3.6 1 1 0 01-.25 1z"/></svg></span>
    PHONE: (555) 014-3380
  </div>
  <div class="item" style="left:835px">
    <span class="dot"><svg width="10" height="8" viewBox="0 0 20 16"><rect x="1" y="1" width="18" height="14" fill="none" stroke="#3e4a8f" stroke-width="2"/><path d="M1 1l9 7 9-7" fill="none" stroke="#3e4a8f" stroke-width="2"/></svg></span>
    EMAIL: info@tallowfieldlaw.example
  </div>
</div>

<header class="abs nav">
  <div class="brand">Tallowfield Hartley</div>
  <span class="menu active" style="left:474px">Home</span>
  <span class="menu" style="left:560px">Family Law</span>
  <span class="menu" style="left:684px">Criminal Law</span>
  <span class="menu" style="left:817px">About Us</span>
  <span class="menu" style="left:928px">Blog</span>
  <span class="menu" style="left:1006px">Contact</span>
</header>

<section class="abs hero" role="img" aria-label="Photo of the two founding partners in suits standing in a bright office">
  <div class="abs hero-name">Tallowfield | Hartley</div>
  <h1 class="abs hero-title">Family Law Practice</h1>
  <p class="abs hero-sub">The law firm of Tallowfield Hartley, LLC is based in Marlow County,<br>conveniently located in Alderbrook</p>
  <div class="btn">CONTACT US</div>
  <div class="abs scroll-tab"><svg class="abs" style="left:13px;top:9px" width="14" height="14" viewBox="0 0 14 14"><circle cx="7" cy="7" r="6" fill="none" stroke="#5a7be0"/><path d="M4.5 6l2.5 2.5L9.5 6" fill="none" stroke="#5a7be0"/></svg></div>
</section>

<section class="abs awards">
  <h2 class="section-title" style="top:44px">Awards Winning Recognition</h2>
  <div class="rule" style="top:101px"></div>
  <div class="badge" style="left:141px;top:134px;width:136px;height:56px;border-radius:4px" role="img" aria-label="Ratings listing badge"></div>
  <div class="badge" style="left:372px;top:136px;width:141px;height:62px;border-radius:2px;background:#f39a2b" role="img" aria-label="Peer-rated lawyers listing badge"></div>
  <div class="badge" style="left:612px;top:131px;width:75px;height:75px;border-radius:50%;background:#cfcfcf" role="img" aria-label="Bar association seal"></div>
  <div class="badge" style="left:786px;top:130px;width:94px;height:77px;border-radius:3px;background:#a9a9a9" role="img" aria-label="Peer-rated lawyers certificate"></div>
  <div class="badge" style="left:980px;top:131px;width:79px;height:79px;border-radius:50%;background:#cfcfcf" role="img" aria-label="Bar association seal"></div>
</section>

<section class="about">
  <div class="abs about-frame"></div>
  <div class="abs about-photo" role="img" aria-label="Photo of a bronze Lady Justice statue beside a lawyer at a desk"></div>
  <div class="abs hatch"></div>
  <div class="abs hatch2"></div>
  <div class="abs years-box">
    <span class="have">Have Over</span>
    <span class="num">30</span>
    <span class="plus">+ Years</span>
    <span class="exp">Experience</span>
  </div>
  <h2 class="abs about-title">About Us</h2>
  <div class="abs about-rule"></div>
  <div class="abs about-text">
    <p>The law firm of Tallowfield Hartley, LLC is based in Marlow County, conveniently located in Alderbrook, Westmarch in 40 Meridian Plaza. We serve the needs of clients throughout Marlow County, as well as, clients from several other counties, including, but not limited to, Ashby, Corwin, Danvers and Elmwood. Between our partners, we have over 30+ years of experience assisting clients with all of their family law and criminal law needs.</p>
    <p>Often times the areas of family law and criminal law cross paths, which can be both emotionally and financially complex. We understand that our client's case is unique and pride ourselves on being responsive to all of our clients needs.</p>
  </div>
  <div class="btn">READ MORE</div>
</section>

<section class="services">
  <div class="abs services-bg"></div>
  <h2 class="section-title" style="top:1548px">Our Law Services</h2>
  <div class="rule" style="top:1600px"></div>
  <div class="tab" style="left:460px;width:133px;background:var(--navy)">FAMILY LAW</div>
  <div class="tab" style="left:607px;width:136px;background:var(--blue)">CRIMINAL LAW</div>

  <div class="arrow-btn" style="left:100px;top:1798px;border:1px solid #888;background:#fff">
    <svg width="24" height="24" viewBox="0 0 24 24"><path d="M14 8l-4 4 4 4" fill="none" stroke="#666" stroke-width="1.5"/></svg>
  </div>
  <div class="arrow-btn" style="left:1081px;top:1798px;background:var(--blue)">
    <svg width="26" height="26" viewBox="0 0 26 26"><path d="M11 9l4 4-4 4" fill="none" stroke="#fff" stroke-width="1.5"/></svg>
  </div>

  <article class="card" style="left:141px">
    <div class="ph" role="img" aria-label="Photo of a gavel in front of a couple removing wedding rings" style="background:linear-gradient(135deg,#d9cfc6,#8a6a52)"></div>
    <h3>Divorce</h3><p>Lorem ipsum dolor sit amet, consectetuer...</p>
  </article>
  <article class="card" style="left:326px">
    <div class="ph" role="img" aria-label="Photo of a young child sitting on a sofa with a parent" style="background:linear-gradient(135deg,#4e5d4a,#b9b2a6)"></div>
    <h3>Child Custody</h3><p>Lorem ipsum dolor sit amet, consectetuer...</p>
  </article>
  <article class="card" style="left:512px">
    <div class="ph" role="img" aria-label="Photo of a child support agreement document with a pen" style="background:linear-gradient(135deg,#eee8dc,#9c3a2c)"></div>
    <h3>Child Support</h3><p>Lorem ipsum dolor sit amet, consectetuer...</p>
  </article>
  <article class="card" style="left:698px">
    <div class="ph" role="img" aria-label="Photo of a gavel on alimony paperwork" style="background:linear-gradient(135deg,#cbb58a,#efe6d0)"></div>
    <h3>Alimony</h3><p>Lorem ipsum dolor sit amet, consectetuer...</p>
  </article>
  <article class="card" style="left:884px">
    <div class="ph" role="img" aria-label="Photo of a distressed couple arguing at home" style="background:linear-gradient(135deg,#e4ddd4,#9d8876)"></div>
    <h3>Domestic violence</h3><p>Lorem ipsum dolor sit amet, consectetuer...</p>
  </article>
</section>

<section class="team">
  <h2 class="section-title" style="top:2003px">Our Team</h2>
  <div class="rule" style="top:2055px"></div>

  <article class="member" style="left:147px">
    <div class="ph" role="img" aria-label="Portrait of partner Martin R. Tallowfield in an office" style="background:linear-gradient(160deg,#8b8378,#4a4e5c)"></div>
    <h4>Martin R. Tallowfield</h4><div class="role">Lorem Ipsum, remps</div>
    <div class="social"><i></i><i></i><i></i><svg width="18" height="13" viewBox="0 0 18 13"><rect x=".5" y=".5" width="17" height="12" fill="none" stroke="#5b6a9e"/><path d="M.5.5l8.5 7 8.5-7" fill="none" stroke="#5b6a9e"/></svg></div>
  </article>
  <article class="member featured" style="left:382px">
    <div class="ph" role="img" aria-label="Portrait of partner Owen P. Hartley at his desk" style="background:linear-gradient(160deg,#6c6256,#2d3240)"></div>
    <h4>Owen P. Hartley</h4><div class="role">Lorem Ipsum, remps</div>
    <div class="social"><i></i><i></i><i></i><svg width="18" height="13" viewBox="0 0 18 13"><rect x=".5" y=".5" width="17" height="12" fill="none" stroke="#5b6a9e"/><path d="M.5.5l8.5 7 8.5-7" fill="none" stroke="#5b6a9e"/></svg></div>
  </article>
  <article class="member" style="left:617px">
    <div class="ph" role="img" aria-label="Portrait of attorney Dana S. Marsh outdoors" style="background:linear-gradient(160deg,#a58a78,#3a3233)"></div>
    <h4>Dana S. Marsh</h4><div class="role">Lorem Ipsum, remps</div>
    <div class="social"><i></i><i></i><i></i><svg width="18" height="13" viewBox="0 0 18 13"><rect x=".5" y=".5" width="17" height="12" fill="none" stroke="#5b6a9e"/><path d="M.5.5l8.5 7 8.5-7" fill="none" stroke="#5b6a9e"/></svg></div>
  </article>
  <article class="member" style="left:852px">
    <div class="ph" role="img" aria-label="Portrait of attorney Lydia K. Verity" style="background:linear-gradient(180deg,#f4f4f4 40%,#2a55c8)"></div>
    <h4>Lydia K. Verity</h4><div class="role">Lorem Ipsum, remps</div>
    <div class="social"><i></i><i></i><i></i><svg width="18" height="13" viewBox="0 0 18 13"><rect x=".5" y=".5" width="17" height="12" fill="none" stroke="#5b6a9e"/><path d="M.5.5l8.5 7 8.5-7" fill="none" stroke="#5b6a9e"/></svg></div>
  </article>
</section>

<section class="abs cta" role="img" aria-label="Blue tinted photo of a gavel on a desk">
  <h2>Tallowfield Hartley Legal Law</h2>
  <div class="cta-rule"></div>
  <p>TO DISCUSS YOUR MATTER WITH EITHER MR. TALLOWFIELD OR MR. HARTLEY SEND US YOUR DETAILS ABOUT YOUR SITUATION OR CONTACT US DIRECTLY AT</p>
  <div class="pill">
    <svg width="22" height="22" viewBox="0 0 24 24"><circle cx="12" cy="12" r="11" fill="none" stroke="#3e4a8f"/><path fill="#3e4a8f" d="M9 7l1.5 2.5-1 1a7 7 0 004 4l1-1L17 15l-1 2c-5 0-9-4-9-9z"/></svg>
    <strong style="font-weight:700">CALL NOW -</strong> <span>(555) 014-3380.</span>
  </div>
</section>

<section class="testimonial">
  <div class="abs t-photo" role="img" aria-label="Photo of a smiling client in a blue shirt against a grey wall"></div>
  <div class="abs t-card">
    <h2>What Our Clients Say?</h2>
    <div class="t-rule"></div>
    <blockquote>Lorem ipsum dolor sit amet, consectetuer adipiscing elit, sed diam nonummy nibh euismod tincidunt ut laoreet dolore magna aliquam erat volutpat. Ut wisi enim ad minim veniam, quis nostrud exerci tation ullamcorper suscipit lobortis nisl ut aliquip ex ea commodo consequat. Duis autem vel eum iriure dolor in hendrerit in vulputate velit esse molestie consequat, vel illum dolore eu feugiat nulla facilisis at vero eros et accumsan et iusto odio dignissim qui blandit praesent luptatum zzril delenit augue duis dolore te feugait nulla facilisi.</blockquote>
    <div class="who">-Theo Rowan</div>
  </div>
  <div class="t-arrow" style="top:3277px;background:var(--navy)"><svg width="18" height="12" viewBox="0 0 18 12"><path d="M1 6h15M11 1l5 5-5 5" fill="none" stroke="#fff" stroke-width="1.5"/></svg></div>
  <div class="t-arrow" style="top:3305px"><svg width="18" height="12" viewBox="0 0 18 12"><path d="M17 6H2M7 1L2 6l5 5" fill="none" stroke="#fff" stroke-width="1.5"/></svg></div>
</section>

<section class="contact-area">
  <div class="abs map" role="img" aria-label="Street map showing the office location"></div>
  <div class="abs map-line"></div>
  <div class="abs contact">
    <h2>CONTACT DETAILS</h2>
    <div class="c-rule"></div>
    <div class="c-item" style="top:130px">
      <svg width="14" height="18" viewBox="0 0 14 18"><path fill="#5a7be0" d="M7 0a7 7 0 017 7c0 5-7 11-7 11S0 12 0 7a7 7 0 017-7z"/><circle cx="7" cy="7" r="2.5" fill="#2d2d2d"/></svg>
      <div><strong style="font-weight:500">Tallowfield &amp; Hartley LLC</strong><br>40 Meridian Plaza Drive Suite 208<br>Alderbrook, WM 09990</div>
    </div>
    <div class="c-item" style="top:212px">
      <svg width="16" height="16" viewBox="0 0 24 24"><path fill="#5a7be0" d="M6.6 10.8a15 15 0 006.6 6.6l2.2-2.2a1 1 0 011-.25 11.4 11.4 0 003.6.6 1 1 0 011 1V20a1 1 0 01-1 1A17 17 0 013 4a1 1 0 011-1h3.5a1 1 0 011 1 11.4 11.4 0 00.6 3.6 1 1 0 01-.25 1z"/></svg>
      <div>(555) 014-3380</div>
    </div>
    <div class="c-item" style="top:260px">
      <svg width="16" height="16" viewBox="0 0 16 16"><rect x="1" y="5" width="14" height="9" rx="1" fill="#5a7be0"/><rect x="4" y="1" width="8" height="5" fill="none" stroke="#5a7be0" stroke-width="1.5"/><rect x="4" y="9" width="8" height="2" fill="#2d2d2d"/></svg>
      <div>(555) 014-3391</div>
    </div>
    <div class="c-item" style="top:318px">
      <svg width="16" height="12" viewBox="0 0 16 12"><rect width="16" height="12" rx="1" fill="#5a7be0"/><path d="M0 0l8 6 8-6" fill="none" stroke="#2d2d2d" stroke-width="1.2"/></svg>
      <div>inquiry@tallowfieldlaw.example</div>
    </div>
  </div>
</section>

<footer>
  <span class="f-link active" style="left:321px">Home</span>
  <span class="f-link" style="left:405px">Family Law</span>
  <span class="f-link" style="left:516px">Criminal Law</span>
  <span class="f-link" style="left:639px">About Us</span>
  <span class="f-link" style="left:740px">Blog</span>
  <span class="f-link" style="left:813px">Contact Us</span>
  <div class="abs f-brand">Tallowfield Hartley</div>
  <p class="abs disclaimer"><strong style="color:#555">Disclaimer:</strong> Lorem ipsum dolor sit amet, consectetuer adipiscing elit, sed diam nonummy nibh euismod tincidunt ut laoreet dolore magna aliquam erat volutpat. Ut wisi enim ad minim veniam, quis nostrud exerci tation ullamcorper suscipit lobortis nisl ut aliquip ex ea commodo consequat.</p>
  <div class="abs bottom">Copyright © 2020 <strong>Tallowfield &amp; Hartley LLC</strong>. All Rights Reserved.</div>
</footer>

</body>
</html>
```